Pellor Autos, LLC Business Card
Business Card
Pellor Autos, LLC Business Card -
Creative Brief
Simple
Marcus Denby
Owner
4471 Brantley Ave Suite K Dalmont, OK 73521
pellorautosllc@brintomail.com
I want a picture of the business logo.

```html
<!DOCTYPE html>
<html lang="en">
<head>
<meta charset="utf-8">
<title>Pellor Autos, LLC Business Card</title>
<link rel="stylesheet" href="https://fonts.googleapis.com/css2?family=Open+Sans:wght@400;600;700&display=swap">
<style>
  :root {
    --stage: #e4e4e6;
    --card: #ffffff;
    --brand-red: #d9111b;
    --brand-red-dark: #a70c13;
    --ink: #1e1e1e;
    --ink-soft: #3a3a3a;
    --rule: #c9c9c9;
  }
  * { margin: 0; padding: 0; box-sizing: border-box; }
  html, body {
    width: 1200px;
    height: 826px;
    overflow: hidden;
    background: var(--stage);
    font-family: "Open Sans", Arial, sans-serif;
  }
  .business-card {
    position: absolute;
    left: 125px;
    top: 139px;
    width: 974px;
    height: 582px;
    border-radius: 30px;
    overflow: hidden;
    background: var(--card);
    box-shadow: 0 10px 30px rgba(0,0,0,0.18);
  }
  .card-accent {
    position: absolute;
    inset: 0;
    width: 974px;
    height: 582px;
  }
  .brand {
    position: absolute;
    left: 158px;
    top: 32px;
    display: flex;
    align-items: center;
    gap: 20px;
  }
  .brand-mark {
    width: 110px;
    height: 110px;
    background: var(--brand-red);
  }
  .brand-name {
    font-weight: 700;
    font-size: 50px;
    letter-spacing: 1px;
    color: var(--ink);
    text-transform: uppercase;
    white-space: nowrap;
  }
  .holder {
    position: absolute;
    right: 103px;
    top: 266px;
    text-align: right;
  }
  .holder-name {
    font-weight: 700;
    font-size: 33px;
    color: var(--brand-red);
    line-height: 1.1;
  }
  .holder-role {
    font-size: 19px;
    color: var(--ink-soft);
    margin-top: 2px;
  }
  .contact {
    position: absolute;
    left: 156px;
    top: 330px;
    font-size: 24px;
    line-height: 36px;
    color: var(--ink);
  }
  .contact .address { margin-bottom: 2px; }
  .contact p { white-space: nowrap; }
</style>
</head>
<body>
  <div class="business-card">
    <svg class="card-accent" viewBox="0 0 974 582" aria-hidden="true">
      <defs>
        <linearGradient id="accentRed" x1="0" y1="0" x2="0" y2="1">
          <stop offset="0" stop-color="#d9111b"/>
          <stop offset="1" stop-color="#a70c13"/>
        </linearGradient>
      </defs>
      <rect width="974" height="582" fill="url(#accentRed)"/>
      <path d="M108 0 H974 V582 H115 C20 450 20 250 108 0 Z" fill="#ffffff"/>
      <path d="M108 0 C20 250 20 450 115 582" fill="none" stroke="#c9c9c9" stroke-width="3"/>
    </svg>

    <div class="brand">
      <div class="brand-mark"></div>
      <div class="brand-name">Pellor Autos, LLC</div>
    </div>

    <div class="holder">
      <p class="holder-name">Marcus Denby</p>
      <p class="holder-role">Owner</p>
    </div>

    <div class="contact">
      <div class="address">
        <p>4471 Brantley Ave Suite K</p>
        <p>Dalmont, OK 73521</p>
      </div>
      <p>P : 2815550142</p>
      <p>C : 8325550178</p>
      <p>F : 2815550143</p>
      <p>E : pellorautosllc@brintomail.com</p>
    </div>
  </div>
</body>
</html>
```